Strong, modern, clean Business Card design

Looking for a stunning, but CLEAN business card design. While we are a faith-based organization, we do NOT want this to look religious.

Industry/Entity Type

Non-Profit

Contact Information for Business Card

Dale Munroe | Lead Pastor
dale@BrightHarvestHope.org
970-555-0148
PO Box 7316
Ashvale, WY 80571

Font styles to use
Serif
Sans Serif

Requirements
Should not have
• Religious imagery or symbolism

```html
<!DOCTYPE html>
<html lang="en">
<head>
<meta charset="utf-8">
<title>Bright Harvest Church – Business Card</title>
<link rel="stylesheet" href="https://fonts.googleapis.com/css2?family=Archivo+Narrow:wght@400;700&display=swap">
<style>
  :root {
    --backdrop: #2a2a2c;
    --card: #050506;
    --accent: #4f7f98;
    --ink: #f2f2f2;
  }
  * { box-sizing: border-box; margin: 0; padding: 0; }
  html, body {
    width: 1200px; height: 1000px; overflow: hidden;
    background: var(--backdrop);
  }
  .stage {
    position: relative; width: 1200px; height: 1000px;
    display: flex; justify-content: center; align-items: center; gap: 80px;
  }
  .card {
    position: relative;
    width: 380px; height: 660px;
    background: var(--card);
    border-radius: 28px;
    box-shadow: 0 18px 40px rgba(0,0,0,.45);
  }
  .brand-name {
    position: absolute; left: 0; right: 0;
    font-family: "Archivo Narrow", sans-serif;
    font-weight: 700;
    color: var(--accent);
    text-transform: uppercase;
    text-align: center;
    letter-spacing: .08em;
    line-height: 1.25;
  }
  .card--front .brand-name { top: 262px; font-size: 38px; }
  .card--back .brand-name { top: 150px; font-size: 32px; }

  .contact {
    position: absolute; left: 56px; top: 400px;
    font-family: "Archivo Narrow", sans-serif;
    color: var(--ink);
  }
  .contact-name {
    font-size: 22px; font-weight: 700; color: var(--accent);
    text-transform: uppercase; letter-spacing: .01em;
  }
  .contact-role { font-size: 15px; margin: 4px 0 24px 4px; }
  .contact-lines {
    list-style: none; padding-left: 40px;
    font-size: 16px; line-height: 1.55;
  }
</style>
</head>
<body>
  <main class="stage">
    <section class="card card--front" aria-label="Card front">
      <p class="brand-name">Bright Harvest<br>Church</p>
    </section>

    <section class="card card--back" aria-label="Card back">
      <p class="brand-name">Bright Harvest<br>Church</p>
      <div class="contact">
        <p class="contact-name">Dale Munroe</p>
        <p class="contact-role">Lead Pastor</p>
        <ul class="contact-lines">
          <li>PO Box 7316&nbsp; Ashvale, WY 80571</li>
          <li>970-555-0148</li>
          <li>dale@BrightHarvestHope.org</li>
        </ul>
      </div>
    </section>
  </main>
</body>
</html>
```